Travel Company is looking for a STAND OUT Business Card

I need a unique Business Card that will truly stand out. Nothing too busy. Simple is good, right? Not looking for a standard design either. No cookie cutter layout. We are a Travel Company that works more with Companies than Travelers. I had an idea to focus and emphasis on the 2 logo a bit more. This is not necessary, however thought it would look interesting. I am just looking for something interesting and a bit different. Does't have to completely off the wall crazy, just not your run of the mill business card.

Target Market(s)

Hoteliers, Resort Management, Call Centers, Executives, Travelers, Families, Businesses

Industry/Entity Type

Hospitality

Contact Information for Business Card

President/CEO - Marco T Villena (title not necessary if design doesn't allow for it)
contact - (407) 555-0182
email - mvillena@roam4ward.example
address - 4127 Brindle Oak Way #164
Orlando, FL 32899
website - www.roam4ward.example

Font styles to use
Serif
Other font styles liked:
• Avenir Next LT Pro BOLD

Requirements
Must have
• simple look and design. Unique design
Nice to have
• I attached the 2 logo separate from the main logo. This can be used separately from the Main Logo, together with the main logo or as main logo. I included the logo font. Use it or not, designers choice.
Should not have
• cookie cutter design. Little use of red other than the logo

```html
<!DOCTYPE html>
<html lang="en">
<head>
<meta charset="utf-8">
<title>Roam4ward Business Card</title>
<link href="https://fonts.googleapis.com/css2?family=Open+Sans:wght@400;600;700;800&display=swap" rel="stylesheet">
<style>
  :root {
    --bg: #e9e6e1;
    --card-white: #ffffff;
    --card-black: #222222;
    --ink: #1b1b1b;
    --red: #e8141b;
    --white: #ffffff;
  }
  * { margin: 0; padding: 0; box-sizing: border-box; }
  html, body {
    width: 1200px; height: 900px; overflow: hidden;
    background: var(--bg);
    font-family: "Open Sans", Arial, sans-serif;
  }
  .canvas { position: relative; width: 1200px; height: 900px; }
  .card {
    position: absolute; width: 600px; height: 343px;
    box-shadow: 0 6px 18px rgba(0,0,0,0.18);
    overflow: hidden;
  }
  .card-back { left: 300px; top: 70px; background: var(--card-black); }
  .card-front { left: 300px; top: 477px; background: var(--card-white); }

  .back-brand {
    position: absolute; inset: 0;
    display: flex; align-items: center; justify-content: center;
    color: var(--white); font-weight: 800; font-size: 62px; letter-spacing: -1px;
  }

  .corner-mark { position: absolute; left: 0; top: 18px; }
  .holder { position: absolute; left: 52px; top: 16px; }
  .holder-name { color: var(--red); font-weight: 700; font-size: 16px; line-height: 1.2; }
  .holder-title { color: var(--ink); font-size: 12px; line-height: 1.3; }

  .contact {
    position: absolute; left: 70px; top: 132px;
    color: var(--ink); font-size: 14px; line-height: 19px;
    list-style: none;
  }
  .contact li { display: flex; align-items: center; }
  .contact .address { padding-left: 22px; }
  .contact svg { width: 12px; height: 12px; margin-right: 10px; flex: none; }

  .front-brand {
    position: absolute; left: 330px; top: 140px;
    color: var(--ink); font-weight: 800; font-size: 44px; letter-spacing: -1px;
  }
  .bands { position: absolute; left: 0; top: 0; }
</style>
</head>
<body>
<main class="canvas">
  <section class="card card-back">
    <div class="back-brand">roam4ward</div>
  </section>

  <section class="card card-front">
    <svg class="corner-mark" width="48" height="22" viewBox="0 0 48 22">
      <polygon points="0,0 20,0 0,22" fill="#1b1b1b"/>
      <polygon points="24,0 48,0 48,22 4,22" fill="#e8141b"/>
    </svg>
    <div class="holder">
      <div class="holder-name">Marco T Villena</div>
      <div class="holder-title">President/CEO</div>
    </div>

    <ul class="contact">
      <li class="address">4127 Brindle Oak Way #164</li>
      <li class="address">Orlando, FL 32899</li>
      <li>
        <svg viewBox="0 0 12 12"><path d="M2.5 1 L4.5 1 L5 3.5 L3.8 4.4 Q5 7 7.6 8.2 L8.5 7 L11 7.5 L11 9.5 Q10.5 11 9 11 Q1 10 1 3 Q1 1.5 2.5 1Z" fill="#e8141b"/></svg>
        (407) 555-0182
      </li>
      <li>
        <svg viewBox="0 0 12 12"><rect x="0.5" y="2" width="11" height="8" fill="#e8141b"/><path d="M0.5 2 L6 6.5 L11.5 2" stroke="#fff" stroke-width="1" fill="none"/></svg>
        mvillena@roam4ward.example
      </li>
      <li>
        <svg viewBox="0 0 12 12"><circle cx="6" cy="6" r="5.5" fill="#e8141b"/><path d="M0.5 6 H11.5 M6 0.5 V11.5 M6 0.5 Q3 6 6 11.5 M6 0.5 Q9 6 6 11.5" stroke="#fff" stroke-width="0.8" fill="none"/></svg>
        www.roam4ward.example
      </li>
    </ul>

    <div class="front-brand">roam4ward</div>

    <svg class="bands" width="600" height="343" viewBox="0 0 600 343">
      <polygon points="0,262 300,262 292,282 0,282" fill="#1b1b1b"/>
      <polygon points="298,288 600,288 600,328 282,328" fill="#e8141b"/>
    </svg>
  </section>
</main>
</body>
</html>
```